Sheriff Candidate needs a large yard sign

A candidate for Sheriff needs to have a sign to put in front of businesses and houses that advertise her candidacy.

Target Market(s)

Democrats, voters

Industry/Entity Type

Political

Font styles to use
Sans Serif

Colors
34a7d7
3276b5

Requirements
Must have
• Must have her picture
• Must have the words "Elect Dana Whitlock" - I'd like the name Dana to be smaller Whitlock. "Elect" and "Whitlock" should be the focus.
• at the bottom in a box "Paid for by the Committee to Elect Dana Whitlock"
Nice to have
• it would be good to have her logo as well.
• blue color for democrats and on a white background
Should not have
• pink color

```html
<!DOCTYPE html>
<html lang="en">
<head>
<meta charset="utf-8">
<title>Elect Dana Whitlock – Yard Sign</title>
<link rel="stylesheet" href="https://fonts.googleapis.com/css2?family=Roboto+Slab:wght@800;900&family=Montserrat:wght@800&display=swap">
<style>
  :root {
    --blue-dark: #3276b5;
    --blue-light: #34a7d7;
    --white: #ffffff;
    --gold: #c9a233;
    --gold-deep: #8a6a14;
    --photo-top: #d9d4cf;
    --photo-bottom: #2a2d3a;
  }
  * { margin: 0; padding: 0; box-sizing: border-box; }
  html, body { width: 848px; height: 1200px; overflow: hidden; background: var(--white); }
  .sign { position: relative; width: 848px; height: 1200px; background: var(--white); overflow: hidden; }

  .candidate-photo {
    position: absolute; left: 0; top: 0; width: 405px; height: 600px;
    background: linear-gradient(180deg, var(--photo-top) 0%, #8f8a86 40%, var(--photo-bottom) 100%);
  }

  .campaign-seal {
    position: absolute; left: 456px; top: 29px; width: 304px; height: 304px;
    border-radius: 50%; background: var(--gold);
    display: flex; align-items: center; justify-content: center; text-align: center;
  }
  .campaign-seal__name {
    font-family: "Roboto Slab", serif; font-weight: 800; font-size: 34px; line-height: 1.15;
    color: var(--white); text-transform: uppercase; letter-spacing: 1px;
  }

  .bands { position: absolute; left: 0; top: 0; width: 848px; height: 960px; }

  .headline-elect {
    position: absolute; left: 140px; top: 512px;
    font-family: "Roboto Slab", serif; font-weight: 900; font-size: 200px; line-height: 1;
    color: var(--white); transform: rotate(-12deg); transform-origin: left bottom;
    letter-spacing: -2px;
  }

  .name-block {
    position: absolute; right: 36px; top: 728px; text-align: right; color: var(--white);
  }
  .name-block__first { font-family: "Montserrat", sans-serif; font-weight: 800; font-size: 54px; line-height: 1; }
  .name-block__last { font-family: "Montserrat", sans-serif; font-weight: 800; font-size: 84px; line-height: 1.05; }

  .disclaimer {
    position: absolute; left: 60px; top: 948px; color: var(--blue-dark);
    font-family: "Montserrat", sans-serif; font-weight: 800;
  }
  .disclaimer__line { font-size: 48px; line-height: 1.2; }
  .disclaimer__elect { font-family: "Roboto Slab", serif; font-weight: 800; font-size: 74px; line-height: 1.15; }
  .disclaimer__first { font-size: 48px; }
</style>
</head>
<body>
<main class="sign">
  <div class="candidate-photo" role="img" aria-label="Portrait photograph of the candidate in a dark blazer"></div>

  <div class="campaign-seal">
    <span class="campaign-seal__name">Whitlock<br>for Sheriff</span>
  </div>

  <svg class="bands" viewBox="0 0 848 960" aria-hidden="true">
    <defs>
      <linearGradient id="band-shadow" x1="0" y1="0" x2="0" y2="1">
        <stop offset="0" stop-color="#000" stop-opacity="0.25"/>
        <stop offset="1" stop-color="#000" stop-opacity="0"/>
      </linearGradient>
    </defs>
    <rect x="0" y="912" width="848" height="14" fill="url(#band-shadow)"/>
    <polygon points="0,591 848,409 848,912 0,912" fill="var(--blue-dark)"/>
    <polygon points="0,841 848,656 848,912 0,912" fill="var(--blue-light)"/>
    <line x1="150" y1="770" x2="700" y2="658" stroke="var(--white)" stroke-width="6"/>
  </svg>

  <div class="headline-elect">Elect</div>

  <div class="name-block">
    <div class="name-block__first">Dana</div>
    <div class="name-block__last">Whitlock</div>
  </div>

  <div class="disclaimer">
    <div class="disclaimer__line">Paid for by the</div>
    <div class="disclaimer__line">Committee to</div>
    <div class="disclaimer__elect">Elect <span class="disclaimer__first">Dana</span> Whitlock</div>
  </div>
</main>
</body>
</html>
```